Forest Consultant/Timber Buyer needs a clean business card

We are a forestry consulting and timber buying company. We meet with private landowners and assist them with timber management and timber harvesting. We would like a professional business card, please no clip art. logo is blue and white but would like to see a gray,silver, or some other color incorporated. Would like basic contact info. Would like to the layout to be creative and sleek but masculine.

Target Market(s)

private landowners

Industry/Entity Type

Business

Contact Information for Business Card

name,position, cell number, office number, email, website. This might be to cluttered. Basic contact info is what we are looking for.

Contact info can all be on one side with logo on the other.

Font styles to use
Serif
Sans Serif

Colors
0255a3
ffffff
aaaaaa

Requirements
Must have
• We just want it professional.
Nice to have
• Creative layout.
Should not have
• please no clip art of log trucks etc.

```html
<!DOCTYPE html>
<html lang="en">
<head>
<meta charset="utf-8">
<title>Stoneway Land &amp; Timber — Business Card</title>
<link rel="stylesheet" href="https://fonts.googleapis.com/css2?family=Open+Sans:wght@400;600;700&display=swap">
<style>
  :root {
    --brand-blue: #0255a3;
    --paper: #ffffff;
    --silver: #aaaaaa;
    --charcoal: #3a3a3c;
    --card-dark: #232324;
    --ink: #333333;
    --backdrop: #e4e2de;
  }
  * { margin: 0; padding: 0; box-sizing: border-box; }
  html, body {
    width: 1200px; height: 950px; overflow: hidden;
    background: var(--backdrop);
    font-family: "Open Sans", Arial, sans-serif;
  }
  .canvas {
    width: 1200px; height: 950px;
    display: flex; flex-direction: column; align-items: center; justify-content: center;
    gap: 34px;
  }
  .card {
    position: relative; width: 760px; height: 434px;
    border-radius: 4px; overflow: hidden;
    box-shadow: 0 6px 18px rgba(0,0,0,.18);
  }
  /* Front */
  .card-front { background: var(--paper); }
  .card-front .wave { position: absolute; inset: 0; width: 100%; height: 100%; }
  .brand {
    position: absolute; left: 56px; top: 150px;
    display: flex; align-items: center; gap: 14px;
  }
  .brand-dot {
    width: 40px; height: 40px; border-radius: 50%;
    background: var(--brand-blue);
  }
  .brand-name {
    font-weight: 700; font-size: 26px; line-height: 1.05;
    color: var(--brand-blue); letter-spacing: .5px;
  }
  .divider {
    position: absolute; left: 372px; top: 44px; width: 1px; height: 170px;
    background: #d8d8d8;
  }
  .contact { position: absolute; left: 398px; top: 48px; color: var(--ink); }
  .contact-name {
    font-weight: 600; font-size: 25px; color: var(--brand-blue);
    letter-spacing: .5px; line-height: 1.1;
  }
  .contact-role { font-size: 17px; letter-spacing: .3px; margin-bottom: 18px; }
  .contact-list { list-style: none; font-size: 15.5px; line-height: 1.65; }
  .contact-list li { display: flex; align-items: center; gap: 10px; }
  .contact-list svg { width: 14px; height: 14px; flex: none; }
  .baseline {
    position: absolute; left: 372px; top: 214px; width: 330px; height: 1px;
    background: #d8d8d8;
  }
  /* Back */
  .card-back { background: var(--card-dark); }
  .back-brand {
    position: absolute; left: 50%; top: 50%; transform: translate(-50%, -50%);
    display: flex; align-items: center; gap: 14px;
  }
  .back-brand .brand-dot { background: var(--paper); width: 34px; height: 34px; }
  .back-brand .brand-name { color: var(--paper); font-size: 28px; }
  .back-url {
    position: absolute; left: 50px; bottom: 44px;
    color: #e6e6e6; font-size: 15px; letter-spacing: 4px;
  }
</style>
</head>
<body>
<main class="canvas">

  <section class="card card-front" aria-label="Business card front">
    <svg class="wave" viewBox="0 0 760 434" preserveAspectRatio="none" aria-hidden="true">
      <path d="M0 300 C160 300 240 340 380 370 C520 400 640 380 760 300 L760 434 L0 434 Z" fill="var(--charcoal)"/>
      <path d="M0 318 C160 318 250 360 390 388 C530 414 650 396 760 322 L760 434 L0 434 Z" fill="var(--brand-blue)"/>
      <path d="M0 336 C170 336 260 378 400 404 C540 428 660 410 760 346 L760 434 L0 434 Z" fill="var(--silver)" opacity=".35"/>
    </svg>

    <div class="brand">
      <span class="brand-dot"></span>
      <span class="brand-name">STONEWAY<br>LAND &amp; TIMBER</span>
    </div>

    <div class="divider"></div>
    <div class="contact">
      <p class="contact-name">DANIEL HARLOW</p>
      <p class="contact-role">CEO/FOUNDER</p>
      <ul class="contact-list">
        <li>
          <svg viewBox="0 0 16 16"><path fill="var(--brand-blue)" d="M3.6 1.5l2.3 2.6-1.3 1.8c.9 2 2.5 3.6 4.5 4.5l1.8-1.3 2.6 2.3-1.4 2.1C6.6 14.9 1.1 9.4 1.5 3z"/></svg>
          555 214 7730
        </li>
        <li>
          <svg viewBox="0 0 16 16"><rect x="4" y="1" width="8" height="14" rx="1.5" fill="none" stroke="var(--brand-blue)" stroke-width="1.6"/></svg>
          555 308 1642
        </li>
        <li>
          <svg viewBox="0 0 16 16"><rect x="1" y="3" width="14" height="10" rx="1" fill="var(--brand-blue)"/><path d="M1.5 4l6.5 5 6.5-5" fill="none" stroke="#fff" stroke-width="1.2"/></svg>
          daniel@stonewaytimber.com
        </li>
        <li>
          <svg viewBox="0 0 16 16"><circle cx="8" cy="8" r="7" fill="var(--brand-blue)"/><path d="M1 8h14M8 1c-3 3-3 11 0 14M8 1c3 3 3 11 0 14" fill="none" stroke="#fff" stroke-width="1"/></svg>
          www.stonewaytimber.com
        </li>
      </ul>
    </div>
    <div class="baseline"></div>
  </section>

  <section class="card card-back" aria-label="Business card back">
    <div class="back-brand">
      <span class="brand-dot"></span>
      <span class="brand-name">STONEWAY</span>
    </div>
    <p class="back-url">www.stonewaytimber.com</p>
  </section>

</main>
</body>
</html>
```